Veltrano - Mechanic/Collision Center Business Card

We're looking for a business card design for our mechanic/ collision repair shop.

Can be with colours or monochromatic.

See the attached files.

Many thanks

```html
<!DOCTYPE html>
<html lang="en">
<head>
<meta charset="utf-8">
<title>Veltrano – Business Card</title>
<link rel="stylesheet" href="https://fonts.googleapis.com/css2?family=Ubuntu:wght@400;700&family=Bodoni+Moda:wght@400&display=swap">
<style>
  :root {
    --brand-blue: #1e9fd9;
    --shadow-grey: #808080;
    --paper: #ffffff;
    --ink: #111111;
  }
  html, body {
    margin: 0;
    padding: 0;
    width: 1200px;
    height: 1000px;
    overflow: hidden;
    background: var(--paper);
    font-family: "Ubuntu", sans-serif;
  }
  .canvas { position: relative; width: 1200px; height: 1000px; }

  .card-shadow { position: absolute; background: var(--shadow-grey); }
  .card { position: absolute; overflow: hidden; }

  /* Front */
  .front-shadow { left: 266px; top: 102px; width: 673px; height: 395px; }
  .card-front { left: 252px; top: 87px; width: 673px; height: 394px; background: var(--brand-blue); }
  .brand-mark {
    position: absolute; left: 0; right: 0; top: 140px;
    display: flex; align-items: center; justify-content: center; gap: 18px;
  }
  .brand-dot { width: 34px; height: 34px; border-radius: 50%; background: var(--paper); }
  .brand-name {
    color: var(--paper); font-weight: 700; font-size: 76px;
    letter-spacing: 2px; line-height: 1; text-transform: uppercase;
  }
  .front-details {
    position: absolute; right: 58px; top: 312px; text-align: right; color: var(--paper);
  }
  .company-name { font-weight: 700; font-size: 18px; margin: 0 0 6px; }
  .company-web { font-weight: 400; font-size: 17px; margin: 0; }

  /* Back */
  .back-shadow { left: 267px; top: 549px; width: 673px; height: 394px; }
  .card-back { left: 252px; top: 531px; width: 673px; height: 396px; background: var(--paper); }
  .symbol-panel {
    position: absolute; left: 448px; top: 0; width: 225px; height: 270px;
    background: var(--brand-blue);
  }
  .person-name {
    position: absolute; left: 48px; top: 38px; margin: 0;
    color: var(--brand-blue); font-weight: 700; font-size: 34px; letter-spacing: 1px;
  }
  .person-role {
    position: absolute; left: 48px; top: 81px; margin: 0;
    font-family: "Bodoni Moda", serif; font-size: 19px; color: var(--ink);
    letter-spacing: 13px;
  }
  .contact-list { position: absolute; left: 48px; top: 185px; margin: 0; width: 420px; }
  .contact-row { position: absolute; left: 0; display: flex; }
  .contact-label {
    width: 162px; color: var(--brand-blue); font-weight: 700; font-size: 24px; line-height: 1;
  }
  .contact-value { margin: 0; color: var(--ink); font-size: 17px; line-height: 22px; }
  .row-phone { top: 0; }
  .row-email { top: 58px; }
  .row-address { top: 105px; }
  .row-postal { top: 146px; }
  .row-phone .contact-value { margin-top: -4px; }
  .row-email .contact-value,
  .row-address .contact-value,
  .row-postal .contact-value { margin-top: 4px; }
</style>
</head>
<body>
<main class="canvas">
  <div class="card-shadow front-shadow"></div>
  <section class="card card-front" aria-label="Card front">
    <div class="brand-mark">
      <span class="brand-dot"></span>
      <span class="brand-name">Veltrano</span>
    </div>
    <div class="front-details">
      <p class="company-name">Veltrano, LDA</p>
      <p class="company-web">www.veltrano-auto.pt</p>
    </div>
  </section>

  <div class="card-shadow back-shadow"></div>
  <section class="card card-back" aria-label="Card back">
    <div class="symbol-panel" role="img" aria-label="Brand symbol area"></div>
    <h1 class="person-name">Tomás Ferraz</h1>
    <p class="person-role">MANAGER</p>
    <div class="contact-list">
      <div class="contact-row row-phone">
        <span class="contact-label">Phone</span>
        <p class="contact-value">+351 912 408 615<br>+351 213 570 284</p>
      </div>
      <div class="contact-row row-email">
        <span class="contact-label">Email</span>
        <p class="contact-value">veltrano.office@mail.pt</p>
      </div>
      <div class="contact-row row-address">
        <span class="contact-label">Address</span>
        <p class="contact-value">Rua das Oficinas, 42</p>
      </div>
      <div class="contact-row row-postal">
        <span class="contact-label">Postal Code</span>
        <p class="contact-value">1900-214 Lisboa</p>
      </div>
    </div>
  </section>
</main>
</body>
</html>
```